Home Delivery Startup needs a web design!

Hello,
We're a start-up company in the final mile logistics industry. Our name is Brightwater Freight Collective. We partner with retailers throughout the USA and Canada and can perform the following services:
Home Delivery
Warehousing
Assembly
We like grey tones and an ability to incorporate our logo and it's colors throughout the site.
We pride ourselves as being a customizable logistics solution .
Our=comprehensive customer support and advanced technology systems make us distinguishable for every delivery solution.
Strategically located distribution centers throughout North America give us an advantage to get product to customers quickly, safely and conveniently, with consistent, efficient service.
Target Market(s)
Retailers in the US and Canada
Industry/Entity Type
Industry
Coding
Coded - Design and coding required
Number of Pages Required
5+ page

```html
<!DOCTYPE html>
<html lang="en">
<head>
<meta charset="utf-8">
<title>Brightwater Freight Collective</title>
<link href="https://fonts.googleapis.com/css2?family=Raleway:wght@400;500;600&family=Open+Sans:ital,wght@0,400;0,600;1,400&display=swap" rel="stylesheet">
<style>
:root{
  --orange:#d2401a;
  --orange-dark:#b42f10;
  --amber:#f39418;
  --amber-light:#f7a51f;
  --ink:#333333;
  --muted:#7a7a7a;
  --rule:#d8d8d8;
  --footer-top:#4a4a4a;
  --footer-bottom:#262626;
  --white:#ffffff;
}
*{box-sizing:border-box;margin:0;padding:0}
html,body{width:1190px;height:1200px;overflow:hidden;background:var(--white)}
body{position:relative;font-family:"Open Sans",sans-serif;color:var(--ink)}
.abs{position:absolute}

.brand{left:206px;top:26px;width:260px;font-family:"Raleway",sans-serif;font-weight:500;font-size:24px;line-height:28px;color:var(--orange)}
.call{right:201px;top:41px;text-align:right;font-family:"Raleway",sans-serif}
.call-label{font-size:14px;color:var(--orange);letter-spacing:.3px}
.call-number{font-size:19px;color:var(--ink);display:flex;align-items:center;gap:5px;margin-top:1px}

.nav{left:0;top:92px;width:1190px;height:41px;background:linear-gradient(#e04a1f,var(--orange-dark));display:flex;justify-content:center}
.nav ul{list-style:none;display:flex;height:100%;margin-left:-2px}
.nav li{font-family:"Raleway",sans-serif;font-weight:600;font-size:13px;color:var(--white);display:flex;align-items:center;padding:0 25px;border-right:1px solid rgba(120,20,0,.55)}
.nav li:last-child{border-right:none}

.hero-band{left:0;top:133px;width:1190px;height:373px;background:linear-gradient(90deg,#dfe8ef 0%,#f2eeea 15%,#f4f4f4 85%,#e9edf0 100%)}
.hero-photo{left:195px;top:133px;width:800px;height:373px;background:linear-gradient(180deg,#f3b456 0%,#d9a26a 18%,#7e8a8e 40%,#6b6f74 65%,#8a5a4a 100%)}
.hero-caption{left:368px;top:259px;width:454px;height:109px;background:rgba(244,138,24,.9);color:var(--white);text-align:center;font-family:"Raleway",sans-serif}
.hero-caption h1{font-weight:500;font-size:26px;margin-top:24px}
.hero-caption p{font-size:19px;margin-top:3px}
.dots{left:563px;top:474px;display:flex;gap:3px}
.dots span{width:14px;height:14px;border-radius:50%;background:var(--white)}

.service{width:251px}
.service-photo{height:118px}
.service h2{font-family:"Raleway",sans-serif;font-weight:400;font-size:17px;margin-top:11px}
.service p{font-size:9px;line-height:16px;color:var(--muted);margin-top:5px}
.btn{display:inline-block;margin-top:10px;width:85px;height:25px;line-height:25px;text-align:center;font-size:9.5px;color:var(--white);background:linear-gradient(var(--amber-light),#e8820f);border-radius:2px;box-shadow:0 1px 2px rgba(0,0,0,.25)}

.divider{left:197px;top:813px;width:798px;height:1px;background:var(--rule)}

.section-title{font-family:"Raleway",sans-serif;font-weight:400;font-size:23px;color:var(--ink)}
.about-photo{left:194px;top:892px;width:150px;height:99px;background:linear-gradient(135deg,#3a7bd0,#d86a3a 55%,#e3a23a)}
.about-lead{left:356px;top:890px;width:360px;font-size:11px;line-height:17px;color:#555}
.about-body{left:356px;top:929px;width:360px;font-size:9px;line-height:16.5px;color:#555}
.about-more{left:194px;top:1004px;width:530px;font-size:9px;line-height:16.5px;color:#555}

.quote{left:752px;top:895px;width:245px;font-style:italic;font-size:10.5px;line-height:19px;color:#555}
.avatar{left:752px;top:979px;width:42px;height:42px;border-radius:50%;background:linear-gradient(#d9b49a,#a9826b)}
.author{left:803px;top:985px;font-size:12px;color:var(--orange)}
.author-place{left:803px;top:1004px;font-size:8.5px;color:#666}

.footer{left:0;top:1094px;width:1190px;height:106px;background:linear-gradient(var(--footer-top),var(--footer-bottom))}
.footer-nav{left:197px;top:1125px;font-family:"Raleway",sans-serif;font-weight:500;font-size:12px;color:var(--white);word-spacing:2px}
.footer-copy{left:197px;top:1146px;font-size:10.5px;color:#ddd}
.social{left:929px;top:1129px;display:flex;gap:4px}
.social span{width:17px;height:17px;border-radius:2px;background:var(--white)}
</style>
</head>
<body>
<header>
  <div class="abs brand">Brightwater Freight<br>Collective</div>
  <div class="abs call">
    <div class="call-label">CALL NOW</div>
    <div class="call-number">
      <svg width="16" height="16" viewBox="0 0 24 24" aria-hidden="true"><path fill="#f39418" d="M6.6 10.8a15.1 15.1 0 0 0 6.6 6.6l2.2-2.2c.3-.3.7-.4 1-.2 1.1.4 2.3.6 3.6.6.6 0 1 .4 1 1V20c0 .6-.4 1-1 1A17 17 0 0 1 3 4c0-.6.4-1 1-1h3.5c.6 0 1 .4 1 1 0 1.3.2 2.5.6 3.6.1.3 0 .7-.2 1z"/></svg>
      555.014.2290
    </div>
  </div>
  <nav class="abs nav">
    <ul>
      <li>HOME</li><li>ABOUT US</li><li>SERVICES</li><li>WAREHOUSE</li><li>BLOG</li><li>TESTIMONIALS</li><li>CONTACT</li>
    </ul>
  </nav>
</header>

<section>
  <div class="abs hero-band" role="img" aria-label="Faded background of cargo containers, an airplane and warehouse workers"></div>
  <div class="abs hero-photo" role="img" aria-label="Aerial view of a container port with cranes, a cargo ship and a highway at sunset"></div>
  <div class="abs hero-caption">
    <h1>Strategically located Distribution</h1>
    <p>centers throughout North America</p>
  </div>
  <div class="abs dots"><span></span><span></span><span></span><span></span></div>
</section>

<section>
  <article class="abs service" style="left:194px;top:537px">
    <div class="service-photo" role="img" aria-label="Courier handing a parcel to a customer at her front door" style="background:linear-gradient(90deg,#6a4a3a,#4f9bd6 55%,#eef2f4)"></div>
    <h2>Home Delivery</h2>
    <p>Aaolutpat Etiam est nunc venenatis in tristique eu impe rdiet ac nisl Cum sociis natoque penatibus nisl Cum sociis natoque penatibus se quam leo molestie</p>
    <span class="btn">READ MORE</span>
  </article>
  <article class="abs service" style="left:474px;top:537px;width:248px">
    <div class="service-photo" role="img" aria-label="Warehouse aisle with tall racks and a forklift" style="background:linear-gradient(90deg,#5a6a8a,#b9a36a 50%,#9aa4b0)"></div>
    <h2>Warehousing</h2>
    <p>Aaolutpat Etiam est nunc venenatis in tristique eu impe rdiet ac nisl Cum sociis natoque penatibus nisl Cum sociis natoque penatibus se quam leo molestie</p>
    <span class="btn">READ MORE</span>
  </article>
  <article class="abs service" style="left:749px;top:537px;width:245px">
    <div class="service-photo" role="img" aria-label="Businesswoman standing in front of stacked shipping containers" style="background:linear-gradient(90deg,#8aa0b8,#3a4050 45%,#b0503a)"></div>
    <h2 style="margin-top:9px">Assembly</h2>
    <p>Aaolutpat Etiam est nunc venenatis in tristique eu impe rdiet ac nisl Cum sociis rdiet ac nisl Cum sociis natoque penatibus se quam leo molestie sed luctus quis</p>
    <span class="btn" style="margin-top:12px">READ MORE</span>
  </article>
</section>

<div class="abs divider"></div>

<section>
  <h2 class="abs section-title" style="left:194px;top:850px">About Our Company</h2>
  <div class="abs about-photo" role="img" aria-label="Colourful stacked shipping containers at a terminal"></div>
  <p class="abs about-lead">Curabitur iaculis tempus eros Curabitur vel mi sit amet magna malesuada ultrices Ut nisi erat fermentum vel congue id euismod</p>
  <p class="abs about-body">feugiat suscipit leo massa sodales velit et scelerisque mi tortor at ipsum cligula augue bibendum accumsan vestibulum ut commodo a mi Morbi ornare gravida elit Integer congue augue et malesuada iaculis ipsum dui aliquet felis at cursus magna nisl nec elit Praesent elementum elit at tellus nec ultricies sit amet porttitor mattis enim</p>
  <p class="abs about-more">In massa libero interdum nec interdum vel blandit sed nulla In ullamcorper est eget tempor cursus neque mi consectetuer mi a ultricies massa est sed nisl Class aptent taciti sociosqu ad litora torquent per conubia nostra per inceptos</p>

  <h2 class="abs section-title" style="left:746px;top:856px">Testimonials</h2>
  <p class="abs quote"><span style="color:#bbb;font-size:18px;font-style:normal">&ldquo;</span> Aorbi ornare gravida elit Integer congue augue et malesuada iaculis ipsum dui aliquet felis at cursus magna nisl nec elit Praesent elementum elit at tellus nec ultricies sit amet porttitor mattis enim <span style="color:#bbb;font-size:18px;font-style:normal">&rdquo;</span></p>
  <div class="abs avatar" role="img" aria-label="Portrait of the reviewer"></div>
  <div class="abs author">By Author Name</div>
  <div class="abs author-place">City, Location Area</div>
</section>

<footer class="abs footer"></footer>
<div class="abs footer-nav">HOME &nbsp;| &nbsp;ABOUT US &nbsp;| &nbsp;SERVICES &nbsp;| &nbsp;TESTIMONIALS &nbsp;| &nbsp;BLOG &nbsp;| &nbsp;CONTACT</div>
<div class="abs footer-copy">&copy; 2015 Company Name &nbsp;All right reserved &nbsp;Term of Use</div>
<div class="abs social" aria-label="Social links"><span></span><span></span><span></span></div>
</body>
</html>
```